Anatomy of Belonging PPT Tempate

Create a Powerpoint template based on The Anatomy of Belonging logo. The Anatomy of Belonging is a methodology and program to help business executives foster resiliency, curiosity, and empathy in managing a globally diverse workforce for business impact (e.g., increased engagement, sales, profits, innovation, and market share, etc.)

Target Market(s)

Business executives

Industry/Entity Type

Business Consultant

Colors

Designer to choose colors to be used in the design.

Requirements
Must have
• * Match the color scheme of logo and tips chart
• * Incorporate a diversity (differences races, ethnic background, religions, etc.) of people on the title slide master
• * Incorporate a diversity (differences races, ethnic background, religions, etc.) of people at the bottom of the section header slide master
Should not have
• * Be silly or cartoonish

```html
<!DOCTYPE html>
<html lang="en">
<head>
<meta charset="utf-8">
<title>Anatomy of Belonging – Presentation Template</title>
<link href="https://fonts.googleapis.com/css2?family=Archivo+Black&family=Open+Sans:wght@400;700&family=PT+Serif:wght@400&display=swap" rel="stylesheet">
<style>
:root{
  --navy:#2b2a5e;
  --gold:#b5883a;
  --mint:#a9d8b8;
  --ink:#2e2e35;
  --body:#5a5a63;
  --canvas:#e9e9ea;
  --paper:#ffffff;
}
*{margin:0;padding:0;box-sizing:border-box}
html,body{width:1200px;height:2201px;overflow:hidden;background:var(--canvas)}
body{position:relative;font-family:"Open Sans",sans-serif;color:var(--ink)}
.abs{position:absolute}

/* hero */
.hero{position:absolute;left:67px;top:50px;width:610px;height:343px;overflow:hidden;box-shadow:0 6px 16px rgba(0,0,0,.35)}
.hero-photo{position:absolute;inset:0;background:linear-gradient(120deg,#2f3a2a 0%,#5f6b4f 35%,#8b8f7a 55%,#3c4635 80%,#1e241c 100%)}
.hero-name{position:absolute;left:381px;top:150px;width:222px;text-align:center;font-family:"Open Sans",sans-serif;font-weight:700;color:#fff;font-size:18px;line-height:1.2}

/* feature list */
.features{position:absolute;left:760px;top:0;width:440px;height:430px;font-family:"Archivo Black",sans-serif;font-size:20px;color:var(--ink)}
.features .line{position:absolute;white-space:nowrap;line-height:1}
.features .box{position:absolute;width:18px;height:20px;border:2.5px solid var(--ink);border-radius:2px;box-shadow:2px 2px 0 var(--ink)}
.features .dot{position:absolute;width:8px;height:8px;background:var(--ink)}

/* slides */
.slide{position:absolute;width:370px;height:208px;background:var(--paper);overflow:hidden;box-shadow:1px 2px 4px rgba(0,0,0,.28)}
.photo{position:absolute}
.title{position:absolute;font-family:"PT Serif",serif;color:var(--navy);font-size:13px;line-height:1.08}
.txt{position:absolute;font-size:4.2px;line-height:1.5;color:var(--body)}
.txt b{color:var(--ink)}
.head{position:absolute;font-size:5.4px;font-weight:700;color:var(--navy);line-height:1.2}
.foot{position:absolute;left:15px;bottom:9px;font-size:3.6px;color:var(--body);white-space:nowrap}
.foot span{margin-left:16px}
.brand{position:absolute;font-family:"Open Sans",sans-serif;font-weight:700;font-size:4px;color:var(--ink);white-space:nowrap}
.brand.tr{right:12px;top:12px}
.brand.tl{left:15px;top:12px}
.brand.br{right:12px;bottom:12px}
.circle{position:absolute;border-radius:50%}
.gold{background:var(--gold)}
.navy{background:var(--navy)}
.mint{background:var(--mint)}
</style>
</head>
<body>

<!-- Title slide -->
<section class="hero">
  <div class="hero-photo" role="img" aria-label="Man running on a treadmill in a bright gym with tall windows"></div>
  <div class="hero-name">The Anatomy of Belonging</div>
</section>

<!-- Feature list -->
<section class="features">
  <span class="box" style="left:0;top:30px"></span><div class="line" style="left:26px;top:33px">Ratio 16:9</div>
  <span class="box" style="left:0;top:60px"></span><div class="line" style="left:26px;top:63px">Full HD</div>
  <span class="box" style="left:0;top:90px"></span><div class="line" style="left:26px;top:93px">Custom color pallet</div>
  <span class="box" style="left:0;top:120px"></span><div class="line" style="left:26px;top:123px">Custom Font -&nbsp; Easy Change</div>
  <span class="box" style="left:0;top:151px"></span><div class="line" style="left:26px;top:154px">Easy to edit, just drag and drop</div>
  <div class="line" style="left:18px;top:181px">images</div>
  <span class="box" style="left:0;top:207px"></span><div class="line" style="left:26px;top:210px">Can be included up to 50</div>
  <div class="line" style="left:18px;top:238px">slides;</div>
  <span class="dot" style="left:58px;top:268px"></span><div class="line" style="left:77px;top:266px">Text + images (1,2,3,4) ,</div>
  <div class="line" style="left:77px;top:293px">Text Slides</div>
  <span class="dot" style="left:58px;top:322px"></span><div class="line" style="left:77px;top:320px">Portfolio Slides , blog slides</div>
  <span class="dot" style="left:58px;top:348px"></span><div class="line" style="left:77px;top:346px">Text Slides, infographics</div>
  <span class="dot" style="left:58px;top:375px"></span><div class="line" style="left:77px;top:373px">Data Slides</div>
  <span class="box" style="left:0;top:398px"></span><div class="line" style="left:26px;top:401px">In the sample you find 22 slides</div>
</section>

<!-- Row 1 -->
<article class="slide" style="left:10px;top:471px">
  <div class="photo" style="left:31px;top:0;width:153px;height:208px;background:linear-gradient(160deg,#8d9094,#5b5f63 60%,#3e4145)" role="img" aria-label="Man holding a side plank on a rooftop"></div>
  <div class="brand tr">The Anatomy of Belonging</div>
  <div class="title" style="left:230px;top:50px;font-size:14px">Agenda</div>
  <div class="txt" style="left:230px;top:72px;font-size:6px;line-height:20.6px;color:var(--ink)">
    <span style="color:var(--gold)">01.</span> <b>Opening ceremony</b><br>
    <span style="color:var(--gold)">02.</span> <b>Speakers Introduction</b><br>
    <span style="color:var(--gold)">03.</span> <b>Opening</b><br>
    <span style="color:var(--gold)">04.</span> <b>Break time</b><br>
    <span style="color:var(--gold)">05.</span> <b>Speakers</b><br>
    <span style="color:var(--gold)">06.</span> <b>Free time</b>
  </div>
</article>

<article class="slide" style="left:413px;top:471px">
  <div class="title" style="left:63px;top:32px">About</div>
  <div class="abs" style="left:63px;top:52px;font-size:8px;font-weight:700;color:var(--navy)">The Anatomy of Belonging</div>
  <div class="txt" style="left:63px;top:85px;width:82px"><b>Leaders who listen first build teams that trust, adapt and grow together</b> across every border, culture and market they serve today.</div>
  <div class="txt" style="left:63px;top:135px;width:82px">Small daily habits of care and <b>open curiosity turn a diverse workforce</b> into a shared source of lasting strength.</div>
  <div class="photo" style="left:248px;top:17px;width:92px;height:138px;background:linear-gradient(150deg,#f1ece6,#c9a488 55%,#6b4a37)" role="img" aria-label="Smiling woman eating a healthy bowl"></div>
  <div class="abs gold" style="left:233px;top:86px;width:30px;height:68px"></div>
  <div class="photo" style="left:154px;top:104px;width:92px;height:104px;background:linear-gradient(160deg,#ece7df,#b68d6d 55%,#d7c25a)" role="img" aria-label="Woman preparing fresh fruit in a kitchen"></div>
  <div class="brand br">The Anatomy of Belonging</div>
</article>

<article class="slide" style="left:816px;top:471px">
  <div class="title" style="left:28px;top:16px">Mission &amp;<br>Vision</div>
  <div class="photo" style="left:102px;top:0;width:268px;height:85px;background:linear-gradient(170deg,#6f9a4a,#4c7a30 60%,#2f5520)" role="img" aria-label="Man resting on a sunny lawn in a park"></div>
  <div class="head" style="left:62px;top:93px;font-size:5px">Mission</div>
  <div class="txt" style="left:62px;top:108px;width:122px"><b>Every leader can learn to lead across difference</b> with steady calm, honest questions and real respect for each person on the team.<br><br>We turn insight into daily practice so that teams feel seen, heard and ready to do their best work.</div>
  <div class="head" style="left:217px;top:93px;font-size:5px">Vision</div>
  <div class="txt" style="left:217px;top:108px;width:122px"><b>A workplace where belonging is a daily habit</b> and where diverse teams grow engagement, ideas and results.<br><br>We see firms that treat inclusion as a core skill, built step by step and measured with care over time.</div>
  <div class="brand br">The Anatomy of Belonging</div>
</article>

<!-- Row 2 -->
<article class="slide" style="left:10px;top:720px">
  <div class="photo" style="left:31px;top:0;width:133px;height:208px;background:linear-gradient(150deg,#6b4a3c,#3a3f55 55%,#1f2233)" role="img" aria-label="Close view of a hand in a training glove"></div>
  <div class="abs gold" style="left:61px;top:35px;width:123px;height:34px"></div>
  <div class="abs" style="left:67px;top:56px;font-size:8px;font-weight:700;color:#fff">Our Values</div>
  <div class="abs" style="left:61px;top:141px;font-size:5px;font-weight:700;color:#fff">Subtitle</div>
  <div class="txt" style="left:61px;top:149px;width:90px;color:#eee">Trust grows when we listen well and lead with steady care for all.</div>
  <div class="brand tr">The Anatomy of Belonging</div>
  <div class="head" style="left:216px;top:40px">Value title here</div>
  <div class="txt" style="left:216px;top:49px;width:132px"><b>Courage to ask honest questions</b> helps teams speak freely and find better answers together.<br><br>It always starts small. A leader who pauses to hear one more view builds a culture where every person feels safe to add ideas.<br><br>It always grows with time.</div>
  <div class="head" style="left:216px;top:129px">Value title here</div>
  <div class="txt" style="left:216px;top:138px;width:132px"><b>Respect for each story</b> lets diverse teams turn differences into fresh ideas and shared wins. When people feel they belong, they stay longer, work harder and care more about the outcome for every client.</div>
</article>

<article class="slide" style="left:413px;top:720px">
  <div class="title" style="left:28px;top:22px">Our Business Philosophy</div>
  <div class="brand tr">The Anatomy of Belonging</div>
  <div class="abs" style="left:31px;top:51px;width:309px;height:32px;box-shadow:1px 1px 2px rgba(0,0,0,.25)"></div>
  <div class="abs navy" style="left:31px;top:51px;width:92px;height:32px"></div>
  <div class="abs" style="left:40px;top:65px;font-size:4.6px;font-weight:700;color:#fff">Element One</div>
  <div class="txt" style="left:134px;top:55px;width:198px"><b>Clear purpose first</b> keeps every decision tied to people and to results. Leaders who set a shared goal help teams move as one, even across many time zones and many cultures at once.</div>
  <div class="abs" style="left:31px;top:95px;width:309px;height:32px;box-shadow:1px 1px 2px rgba(0,0,0,.25)"></div>
  <div class="abs gold" style="left:31px;top:95px;width:92px;height:32px"></div>
  <div class="abs" style="left:40px;top:109px;font-size:4.6px;font-weight:700;color:#fff">Element Two</div>
  <div class="txt" style="left:134px;top:99px;width:198px"><b>Curious listening</b> opens the door to new views. When managers ask before they tell, teams share risks early and build ideas that serve a wider market.</div>
  <div class="abs" style="left:31px;top:138px;width:309px;height:32px;box-shadow:1px 1px 2px rgba(0,0,0,.25)"></div>
  <div class="abs mint" style="left:31px;top:138px;width:92px;height:32px"></div>
  <div class="abs" style="left:40px;top:152px;font-size:4.6px;font-weight:700;color:var(--navy)">Element Three</div>
  <div class="txt" style="left:134px;top:142px;width:198px"><b>Steady empathy</b> turns friction into trust. Teams that feel understood recover faster from change and keep their focus on the work that matters most.</div>
  <div class="foot">The Anatomy of Belonging<span>Page 8</span></div>
</article>

<article class="slide" style="left:816px;top:720px">
  <div class="brand tr">The Anatomy of Belonging</div>
  <div class="title" style="left:62px;top:40px">What it<br>Means</div>
  <div class="head" style="left:60px;top:89px;font-size:5px;color:var(--ink)">Subtitle</div>
  <div class="txt" style="left:60px;top:97px;width:60px"><b>Belonging is built by daily acts</b> of care, honest talk and shared goals across every team and every role.</div>
  <div class="circle" style="left:125px;top:44px;width:120px;height:120px;background:linear-gradient(140deg,#7c7b86,#4b4a6a)" role="img" aria-label="Group of people meditating together"></div>
  <div class="circle" style="left:125px;top:44px;width:120px;height:120px;background:rgba(43,42,94,.55)"></div>
  <div class="abs" style="left:150px;top:99px;width:70px;text-align:center;font-size:6px;font-weight:700;color:#fff;line-height:1.1">Philosophy<br>of Belonging</div>
  <div class="circle gold" style="left:215px;top:28px;width:64px;height:64px;text-align:center;color:#fff">
    <svg width="10" height="10" viewBox="0 0 10 10" style="margin-top:10px"><path d="M1 5h3l1-3 2 6 1-3h1" fill="none" stroke="#fff" stroke-width="1"/></svg>
    <div style="font-size:5.4px;font-weight:700">Resilience</div>
    <div style="font-size:3.4px;line-height:1.4">A steady mind<br>under change.</div>
  </div>
  <div class="circle gold" style="left:263px;top:75px;width:64px;height:64px;text-align:center;color:#fff">
    <svg width="10" height="10" viewBox="0 0 10 10" style="margin-top:10px"><circle cx="4.3" cy="4.3" r="3" fill="none" stroke="#fff" stroke-width="1"/><path d="M6.5 6.5L9 9" stroke="#fff" stroke-width="1"/></svg>
    <div style="font-size:5.4px;font-weight:700">Curiosity</div>
    <div style="font-size:3.4px;line-height:1.4">Ask first, then<br>learn more.</div>
  </div>
  <div class="circle gold" style="left:215px;top:121px;width:64px;height:64px;text-align:center;color:#fff">
    <svg width="10" height="10" viewBox="0 0 10 10" style="margin-top:10px"><path d="M5 8.5L1.5 5A2 2 0 0 1 5 2.5 2 2 0 0 1 8.5 5z" fill="none" stroke="#fff" stroke-width="1"/></svg>
    <div style="font-size:5.4px;font-weight:700">Empathy</div>
    <div style="font-size:3.4px;line-height:1.4">Feel what others<br>face each day.</div>
  </div>
</article>

<!-- Row 3 -->
<article class="slide" style="left:10px;top:970px">
  <div class="title" style="left:28px;top:23px">What We Do?</div>
  <div class="brand tr">The Anatomy of Belonging</div>
  <div class="circle gold" style="left:61px;top:78px;width:40px;height:40px"><svg width="40" height="40" viewBox="0 0 40 40"><path d="M14 21l6-6 6 6M16 20v7h8v-7" fill="none" stroke="#fff" stroke-width="1"/></svg></div>
  <div class="circle gold" style="left:134px;top:78px;width:40px;height:40px"><svg width="40" height="40" viewBox="0 0 40 40"><path d="M15 13h10M15 27h10M16 13l8 14M24 13l-8 14" fill="none" stroke="#fff" stroke-width="1"/></svg></div>
  <div class="circle gold" style="left:206px;top:78px;width:40px;height:40px"><svg width="40" height="40" viewBox="0 0 40 40"><circle cx="20" cy="20" r="6" fill="none" stroke="#fff" stroke-width="1" stroke-dasharray="2 2"/></svg></div>
  <div class="circle gold" style="left:279px;top:78px;width:40px;height:40px"><svg width="40" height="40" viewBox="0 0 40 40"><path d="M14 15h12l-6 12z" fill="none" stroke="#fff" stroke-width="1"/></svg></div>
  <div class="head" style="left:61px;top:124px;font-size:5px;color:var(--ink)">Layered PPT</div>
  <div class="txt" style="left:61px;top:132px;width:58px">Each layer is easy to move, resize and edit for your own story.</div>
  <div class="head" style="left:134px;top:124px;font-size:5px;color:var(--ink)">24/7 Help</div>
  <div class="txt" style="left:134px;top:132px;width:58px">Our team is ready to answer your questions at any hour.</div>
  <div class="head" style="left:206px;top:124px;font-size:5px;color:var(--ink)">Low price</div>
  <div class="txt" style="left:206px;top:132px;width:58px">A fair price that fits a small team or a large firm alike.</div>
  <div class="head" style="left:279px;top:124px;font-size:5px;color:var(--ink)">Freebies Soon</div>
  <div class="txt" style="left:279px;top:132px;width:58px">New free slides and icons will arrive with each update.</div>
  <div class="foot">The Anatomy of Belonging<span>Page 10</span></div>
</article>

<article class="slide" style="left:413px;top:970px">
  <div class="brand tl">The Anatomy of Belonging</div>
  <div class="title" style="left:62px;top:40px">Analisys Slides</div>
  <svg class="abs" style="left:62px;top:66px" width="11" height="11" viewBox="0 0 11 11"><rect x="1" y="3" width="9" height="7" fill="none" stroke="#555" stroke-width=".8"/><path d="M3 3V1h5v2" fill="none" stroke="#555" stroke-width=".8"/></svg>
  <div class="head" style="left:62px;top:81px;font-size:5px;color:var(--ink)">Creation</div>
  <div class="txt" style="left:62px;top:89px;width:68px">Shape fresh ideas with a team that feels free to speak.</div>
  <svg class="abs" style="left:154px;top:66px" width="11" height="11" viewBox="0 0 11 11"><circle cx="5.5" cy="5.5" r="4.5" fill="none" stroke="#555" stroke-width=".8"/><circle cx="5.5" cy="5.5" r="2" fill="none" stroke="#555" stroke-width=".8"/></svg>
  <div class="head" style="left:154px;top:81px;font-size:5px;color:var(--ink)">Web Design</div>
  <div class="txt" style="left:154px;top:89px;width:68px">Build clear pages that welcome every kind of visitor with ease.</div>
  <svg class="abs" style="left:62px;top:127px" width="11" height="11" viewBox="0 0 11 11"><rect x="1" y="3" width="9" height="6" fill="none" stroke="#555" stroke-width=".8"/><circle cx="5.5" cy="6" r="1.5" fill="none" stroke="#555" stroke-width=".8"/></svg>
  <div class="head" style="left:62px;top:141px;font-size:5px;color:var(--ink)">Supporting</div>
  <div class="txt" style="left:62px;top:149px;width:68px">Stand beside each leader as new habits take root.</div>
  <svg class="abs" style="left:154px;top:127px" width="11" height="11" viewBox="0 0 11 11"><path d="M2 9l1-3 5-5 2 2-5 5z" fill="none" stroke="#555" stroke-width=".8"/></svg>
  <div class="head" style="left:154px;top:141px;font-size:5px;color:var(--ink)">Maintenance</div>
  <div class="txt" style="left:154px;top:149px;width:68px">Keep progress on track with steady checks.</div>
  <div class="photo" style="left:248px;top:0;width:122px;height:208px;background:linear-gradient(170deg,#c8ccd2,#7a8aa3 45%,#2c3d8a 70%,#3a3a3a)" role="img" aria-label="Older man running a city race"></div>
  <div class="foot">The Anatomy of Belonging<span>Page 12</span></div>
</article>

<article class="slide" style="left:816px;top:970px">
  <div class="brand tr">The Anatomy of Belonging</div>
  <div class="title" style="left:28px;top:30px">Three column</div>
  <div class="abs" style="left:63px;top:58px;width:88px;height:118px;border-top:1.5px solid var(--gold);box-shadow:1px 1px 2px rgba(0,0,0,.2)"></div>
  <div class="abs" style="left:158px;top:58px;width:88px;height:118px;border-top:1.5px solid var(--navy);box-shadow:1px 1px 2px rgba(0,0,0,.2)"></div>
  <div class="abs" style="left:253px;top:58px;width:88px;height:118px;border-top:1.5px solid var(--mint);box-shadow:1px 1px 2px rgba(0,0,0,.2)"></div>
  <div class="head" style="left:70px;top:64px;font-size:5px;color:var(--ink)">Bullet points &amp;<br>Title here</div>
  <div class="txt" style="left:70px;top:78px;width:74px">1.&nbsp; Open each meeting with one honest question for all.<br>2.&nbsp; Share credit in public and give feedback with care.<br>3.&nbsp; Invite the quiet voice before you close a topic.</div>
  <div class="head" style="left:165px;top:64px;font-size:5px;color:var(--ink)">Bullet points &amp;<br>Title here</div>
  <div class="txt" style="left:165px;top:78px;width:74px">1.&nbsp; Learn the names and stories of your team.<br>2.&nbsp; Ask first.<br>3.&nbsp; Map the skills each person brings.<br>4.&nbsp; Set goals that reflect many views.<br>5.&nbsp; Review results together.</div>
  <div class="head" style="left:260px;top:64px;font-size:5px;color:var(--ink)">Bullet points &amp;<br>Title here</div>
  <div class="txt" style="left:260px;top:78px;width:74px">1.&nbsp; Notice how change lands on each person.<br>2.&nbsp; Pause often.<br>3.&nbsp; Keep promises small and clear.<br>4.&nbsp; Celebrate steady progress.<br>5.&nbsp; Reflect and adjust.</div>
  <div class="foot">The Anatomy of Belonging<span>Page 18</span></div>
</article>

<!-- Row 4 -->
<article class="slide" style="left:10px;top:1219px">
  <div class="title" style="left:28px;top:17px">Four column<br>Images Slide</div>
  <div class="brand tr">The Anatomy of Belonging</div>
  <div class="abs" style="left:61px;top:67px;width:67px;height:117px;box-shadow:1px 1px 2px rgba(0,0,0,.2)"></div>
  <div class="photo" style="left:61px;top:67px;width:67px;height:64px;background:linear-gradient(160deg,#eef0f2,#c7c9cc 60%,#9a9ea4)" role="img" aria-label="Older man stretching in bed"></div>
  <div class="abs" style="left:68px;top:134px;width:20px;height:5px;border-radius:3px;background:#c9c9cc"></div>
  <div class="head" style="left:68px;top:142px;font-size:4.6px;color:var(--ink)">All their<br>equipment and<br>instruments</div>
  <div class="abs" style="left:132px;top:67px;width:67px;height:117px;box-shadow:1px 1px 2px rgba(0,0,0,.2)"></div>
  <div class="photo" style="left:132px;top:67px;width:67px;height:64px;background:linear-gradient(160deg,#e6ebee,#b9c3c6 60%,#8c979c)" role="img" aria-label="Woman stretching by a window"></div>
  <div class="abs" style="left:139px;top:134px;width:20px;height:5px;border-radius:3px;background:#c9a46b"></div>
  <div class="head" style="left:139px;top:142px;font-size:4.6px;color:var(--ink)">All their<br>equipment and<br>instruments are<br>alive.</div>
  <div class="abs" style="left:202px;top:67px;width:67px;height:117px;box-shadow:1px 1px 2px rgba(0,0,0,.2)"></div>
  <div class="photo" style="left:202px;top:67px;width:67px;height:64px;background:linear-gradient(160deg,#eceae7,#bdb7ae 60%,#7d7a78)" role="img" aria-label="Man waking up and stretching"></div>
  <div class="abs" style="left:209px;top:134px;width:20px;height:5px;border-radius:3px;background:#c9c9cc"></div>
  <div class="head" style="left:209px;top:142px;font-size:4.6px;color:var(--ink)">All their<br>equipment and<br>instruments.</div>
  <div class="abs" style="left:272px;top:67px;width:67px;height:117px;box-shadow:1px 1px 2px rgba(0,0,0,.2)"></div>
  <div class="photo" style="left:272px;top:67px;width:67px;height:64px;background:linear-gradient(160deg,#f1efec,#d3c8bd 60%,#a79788)" role="img" aria-label="Woman stretching in a bright bedroom"></div>
  <div class="abs" style="left:279px;top:134px;width:20px;height:5px;border-radius:3px;background:#c9a46b"></div>
  <div class="head" style="left:279px;top:142px;font-size:4.6px;color:var(--ink)">All their<br>equipment and<br>instruments are<br>alive.</div>
  <div class="foot">The Anatomy of Belonging<span>Page 13</span></div>
</article>

<article class="slide" style="left:413px;top:1219px">
  <div class="brand tr">The Anatomy of Belonging</div>
  <div class="photo" style="left:62px;top:17px;width:98px;height:86px;background:linear-gradient(170deg,#d9dde2,#aab2bc 55%,#8a6e62)" role="img" aria-label="Woman in a yoga pose on a city rooftop"></div>
  <div class="abs gold" style="left:160px;top:34px;width:120px;height:68px"></div>
  <div class="abs" style="left:169px;top:68px;font-family:'PT Serif',serif;font-size:12px;color:#fff;line-height:1">Topics</div>
  <div class="abs" style="left:169px;top:83px;font-family:'PT Serif',serif;font-size:7px;color:#fff">Two Images Slide</div>
  <div class="txt" style="left:62px;top:109px;width:97px"><b>Teams thrive when leaders</b> make room for every view and treat each story with respect.<br><br>Short daily rituals of care, clear goals and honest praise help a diverse group feel at home and ready to give its best.</div>
  <div class="photo" style="left:185px;top:104px;width:155px;height:104px;background:linear-gradient(160deg,#c4a98c,#8d6f57 55%,#5b4a46)" role="img" aria-label="Two people meditating in a studio"></div>
  <div class="foot">The Anatomy of Belonging<span>Page 14</span></div>
</article>

<article class="slide" style="left:816px;top:1219px">
  <div class="brand tr">The Anatomy of Belonging</div>
  <div class="title" style="left:28px;top:17px">Bullets<br>Slides</div>
  <div class="head" style="left:33px;top:73px;font-size:5.4px;color:var(--ink)">Subtitle</div>
  <div class="txt" style="left:33px;top:82px;width:100px"><b>Inclusion is a skill that grows with use.</b> Each week leaders can try one new habit and watch trust rise across the whole team.<br><br>Listen, ask and act with care so that people of every background feel they belong and can shape the work they do.</div>
  <div class="circle gold" style="left:186px;top:37px;width:24px;height:24px"><svg width="24" height="24" viewBox="0 0 24 24"><path d="M8 12l3 3 5-6" fill="none" stroke="#fff" stroke-width="1"/></svg></div>
  <div class="head" style="left:219px;top:38px;font-size:4.8px">Flexible Refund Policy</div>
  <div class="txt" style="left:219px;top:46px;width:120px"><b>Change your plan at any time</b> with a simple note to our team and a clear reply.</div>
  <div class="circle gold" style="left:186px;top:75px;width:24px;height:24px"><svg width="24" height="24" viewBox="0 0 24 24"><path d="M8 12l3 3 5-6" fill="none" stroke="#fff" stroke-width="1"/></svg></div>
  <div class="head" style="left:219px;top:76px;font-size:4.8px">Fast and Secure</div>
  <div class="txt" style="left:219px;top:84px;width:120px"><b>Your files stay safe</b> and ready whenever your team needs them most.</div>
  <div class="circle gold" style="left:186px;top:114px;width:24px;height:24px"><svg width="24" height="24" viewBox="0 0 24 24"><path d="M8 12l3 3 5-6" fill="none" stroke="#fff" stroke-width="1"/></svg></div>
  <div class="head" style="left:219px;top:115px;font-size:4.8px">Top Quality</div>
  <div class="txt" style="left:219px;top:123px;width:120px"><b>Every slide is built with care</b> and tested on screens of every size.</div>
  <div class="circle gold" style="left:186px;top:152px;width:24px;height:24px"><svg width="24" height="24" viewBox="0 0 24 24"><path d="M8 12l3 3 5-6" fill="none" stroke="#fff" stroke-width="1"/></svg></div>
  <div class="head" style="left:219px;top:153px;font-size:4.8px">24/7 Professional Support</div>
  <div class="txt" style="left:219px;top:161px;width:120px"><b>Help is always close</b> for any question, large or small, day or night.</div>
  <div class="foot">The Anatomy of Belonging<span>Page 9</span></div>
</article>

<!-- Row 5 -->
<article class="slide" style="left:10px;top:1468px">
  <div class="brand tl">The Anatomy of Belonging</div>
  <div class="title" style="left:62px;top:34px">Problem Analysis</div>
  <div class="txt" style="left:62px;top:59px;width:128px"><b>Where does belonging break down?</b> We look at how teams talk, decide and share credit. Gaps in trust often hide in small habits. Naming them is the first step to fix them and to build a place where every person can add value.</div>
  <div class="abs" style="left:61px;top:122px;width:123px;height:16px;box-shadow:1px 1px 2px rgba(0,0,0,.2)"></div>
  <div class="abs gold" style="left:61px;top:122px;width:92px;height:16px"></div>
  <div class="abs" style="left:66px;top:127px;font-size:3.4px;color:#fff">Element One</div>
  <div class="abs" style="left:138px;top:126px;font-size:5px;font-weight:700;color:#fff">75%</div>
  <div class="abs" style="left:61px;top:144px;width:123px;height:16px;box-shadow:1px 1px 2px rgba(0,0,0,.2)"></div>
  <div class="abs navy" style="left:61px;top:144px;width:62px;height:16px"></div>
  <div class="abs" style="left:66px;top:149px;font-size:3.4px;color:#fff">Element Two</div>
  <div class="abs" style="left:108px;top:148px;font-size:5px;font-weight:700;color:#fff">50%</div>
  <div class="abs" style="left:61px;top:167px;width:123px;height:16px;box-shadow:1px 1px 2px rgba(0,0,0,.2)"></div>
  <div class="abs mint" style="left:61px;top:167px;width:111px;height:16px"></div>
  <div class="abs" style="left:66px;top:172px;font-size:3.4px;color:#fff">Element Three</div>
  <div class="abs" style="left:157px;top:171px;font-size:5px;font-weight:700;color:#fff">90%</div>
  <div class="photo" style="left:216px;top:0;width:154px;height:208px;background:linear-gradient(150deg,#8a5a3e,#c06a3a 30%,#3a3f55 60%,#1e2030)" role="img" aria-label="Close view of a hand in a training glove"></div>
  <div class="foot">The Anatomy of Belonging<span>Page 16</span></div>
</article>

<article class="slide" style="left:413px;top:1468px">
  <div class="title" style="left:31px;top:19px">SWOT Project Analisys</div>
  <div class="brand tr">The Anatomy of Belonging</div>
  <div class="abs" style="left:31px;top:56px;width:78px;border-top:1.5px solid var(--navy)"></div>
  <div class="head" style="left:42px;top:62px;font-size:5.4px;color:var(--ink)">Strengths</div>
  <div class="txt" style="left:42px;top:70px;width:64px">Strong trust and a shared goal across teams.</div>
  <div class="abs" style="left:262px;top:56px;width:78px;border-top:1.5px solid var(--gold)"></div>
  <div class="head" style="left:269px;top:62px;font-size:5.4px;color:var(--ink)">Weaknesses</div>
  <div class="txt" style="left:269px;top:70px;width:64px">Few habits yet for hearing quiet voices.</div>
  <div class="abs" style="left:31px;top:135px;width:78px;border-top:1.5px solid var(--mint)"></div>
  <div class="head" style="left:42px;top:141px;font-size:5.4px;color:var(--ink)">Opportunities</div>
  <div class="txt" style="left:42px;top:149px;width:64px">New markets open when teams think wider.</div>
  <div class="abs" style="left:262px;top:135px;width:78px;border-top:1.5px solid var(--navy)"></div>
  <div class="head" style="left:269px;top:141px;font-size:5.4px;color:var(--ink)">Threats</div>
  <div class="txt" style="left:269px;top:149px;width:64px">Fast change can strain trust and focus.</div>
  <div class="circle" style="left:119px;top:46px;width:132px;height:132px;background:#fff;box-shadow:0 0 3px rgba(0,0,0,.2)"></div>
  <div class="circle" style="left:125px;top:52px;width:120px;height:120px;background:linear-gradient(140deg,#c9a07e,#7a5a48 55%,#3b3a48)" role="img" aria-label="Diverse team working together around a laptop"></div>
  <div class="circle" style="left:155px;top:82px;width:60px;height:60px;background:#fff"></div>
  <div class="abs" style="left:155px;top:104px;width:60px;text-align:center;font-family:'PT Serif',serif;font-size:13px;color:var(--ink)">SWOT</div>
  <div class="circle navy" style="left:116px;top:64px;width:18px;height:18px;color:#fff;text-align:center;font-family:'PT Serif',serif;font-size:9px;line-height:18px">S</div>
  <div class="circle gold" style="left:237px;top:64px;width:18px;height:18px;color:#fff;text-align:center;font-family:'PT Serif',serif;font-size:9px;line-height:18px">W</div>
  <div class="circle mint" style="left:116px;top:143px;width:18px;height:18px;color:var(--navy);text-align:center;font-family:'PT Serif',serif;font-size:9px;line-height:18px">O</div>
  <div class="circle navy" style="left:237px;top:143px;width:18px;height:18px;color:#fff;text-align:center;font-family:'PT Serif',serif;font-size:9px;line-height:18px">T</div>
  <div class="foot">The Anatomy of Belonging<span>Page 15</span></div>
</article>

<article class="slide" style="left:816px;top:1468px">
  <div class="photo" style="left:32px;top:0;width:154px;height:208px;background:linear-gradient(170deg,#3c6e7a,#2c5a66 50%,#1c3f4a)" role="img" aria-label="Player on a sports court in motion"></div>
  <div class="brand tr">The Anatomy of Belonging</div>
  <div class="title" style="left:217px;top:33px">Left image &amp;<br>number slide</div>
  <div class="abs" style="left:217px;top:75px;font-family:'PT Serif',serif;font-size:24px;color:var(--navy)">1</div>
  <div class="head" style="left:240px;top:76px;font-size:5px">Number Title here</div>
  <div class="txt" style="left:240px;top:85px;width:100px">Start each week with a clear goal that the whole team can see.</div>
  <div class="abs" style="left:217px;top:114px;font-family:'PT Serif',serif;font-size:24px;color:var(--navy)">2</div>
  <div class="head" style="left:240px;top:115px;font-size:5px">Number Title here</div>
  <div class="txt" style="left:240px;top:124px;width:100px">Ask each person what help they need to reach that goal.</div>
  <div class="abs" style="left:217px;top:154px;font-family:'PT Serif',serif;font-size:24px;color:var(--navy)">3</div>
  <div class="head" style="left:240px;top:155px;font-size:5px">Number Title here</div>
  <div class="txt" style="left:240px;top:164px;width:100px">Close the week by sharing wins and lessons as one team.</div>
</article>

<!-- Row 6 -->
<article class="slide" style="left:10px;top:1718px">
  <div class="brand tl">The Anatomy of Belonging</div>
  <div class="title" style="left:62px;top:42px">Right Image<br>in text</div>
  <div class="head" style="left:62px;top:77px;font-size:5px;color:var(--ink)">Subtitle</div>
  <div class="txt" style="left:62px;top:85px;width:140px"><b>Belonging starts with one honest talk.</b> When a leader asks how people truly feel, the answer often opens a path to new trust. Small signs of respect, repeated each day, turn a group of strangers into a team that looks out for one another and takes bold steps together.<br><br>Over months these habits shape a culture where people stay, grow and bring their full skill to work. The results show up in engagement, new ideas and a steady rise in sales across every region served.</div>
  <div class="photo" style="left:216px;top:0;width:154px;height:208px;background:linear-gradient(160deg,#c5c8c3,#a3a79f 50%,#6d6f6c)" role="img" aria-label="Man stretching after waking up in a calm bedroom"></div>
  <div class="foot">The Anatomy of Belonging<span>Page 19</span></div>
</article>

<article class="slide" style="left:413px;top:1718px">
  <div class="photo" style="left:31px;top:0;width:185px;height:208px;background:linear-gradient(150deg,#6a3e34,#b47d68 45%,#e7d1c5 75%,#d9c0b3)" role="img" aria-label="Woman resting peacefully with eyes closed"></div>
  <div class="brand tr">The Anatomy of Belonging</div>
  <div class="title" style="left:208px;top:40px">Our Statistic</div>
  <svg class="abs" style="left:150px;top:60px" width="80" height="110" viewBox="0 0 80 110"><path d="M56 6C70 20 72 80 56 104" fill="none" stroke="var(--navy)" stroke-width=".8"/><circle cx="65" cy="12" r="1.6" fill="var(--navy)"/><circle cx="72" cy="56" r="1.6" fill="var(--navy)"/><circle cx="63" cy="98" r="1.6" fill="var(--navy)"/></svg>
  <div class="circle" style="left:159px;top:79px;width:52px;height:52px;background:#fff"></div>
  <div class="circle navy" style="left:164px;top:84px;width:42px;height:42px;color:#fff;text-align:center;font-size:9px;font-weight:700;line-height:42px">50%</div>
  <div class="head" style="left:243px;top:63px;font-size:5px;color:var(--ink)">Title One</div>
  <div class="txt" style="left:243px;top:72px;width:100px"><b>Half of staff</b> say they feel they truly belong at work today.</div>
  <div class="head" style="left:243px;top:107px;font-size:5px;color:var(--ink)">Title Two</div>
  <div class="txt" style="left:243px;top:116px;width:100px"><b>Teams that feel seen</b> share new ideas twice as often as others.</div>
  <div class="head" style="left:243px;top:146px;font-size:5px;color:var(--ink)">Title Three</div>
  <div class="txt" style="left:243px;top:155px;width:100px"><b>Leaders who listen</b> keep their best people for longer terms.</div>
</article>

<article class="slide" style="left:816px;top:1718px">
  <div class="photo" style="left:32px;top:0;width:154px;height:208px;background:linear-gradient(160deg,#dfe3e6,#c3c8cc 50%,#9ea3a8)" role="img" aria-label="Smiling older man stretching in bed"></div>
  <div class="brand tr">The Anatomy of Belonging</div>
  <div class="title" style="left:217px;top:33px">Left Image<br>in text</div>
  <div class="head" style="left:217px;top:77px;font-size:5px;color:var(--ink)">Subtitle</div>
  <div class="txt" style="left:217px;top:85px;width:136px"><b>Curiosity keeps a team alive.</b> Leaders who ask why, and then truly listen, find ideas that no single mind could reach alone. It lifts morale and helps people from many places feel part of one shared goal.<br><br>With time, these small moments build a strong and steady culture. People bring their full selves to work, and the whole firm gains from the range of views, skills and stories they carry with them.</div>
</article>

<!-- Row 7 -->
<article class="slide" style="left:10px;top:1967px">
  <div class="brand tl">The Anatomy of Belonging</div>
  <div class="title" style="left:32px;top:39px">Growth<br>Overview</div>
  <div class="photo" style="left:216px;top:0;width:154px;height:208px;background:linear-gradient(170deg,#e8e6e6,#cfcacc 50%,#8e7f86)" role="img" aria-label="Woman in a yoga pose with arms raised"></div>
  <div class="abs navy" style="left:61px;top:126px;width:68px;height:66px;color:#fff;padding:10px 11px">
    <div style="font-family:'PT Serif',serif;font-size:13px">20%</div>
    <div style="font-size:4.2px;margin-top:4px">Individual</div>
    <div style="font-size:3.6px;line-height:1.4;margin-top:4px">Each person sees a clear path to grow.</div>
  </div>
  <div class="abs mint" style="left:132px;top:85px;width:68px;height:80px;color:var(--navy);padding:10px 11px">
    <div style="font-family:'PT Serif',serif;font-size:13px">60%</div>
    <div style="font-size:4.2px;margin-top:4px">Businesses</div>
    <div style="font-size:3.6px;line-height:1.4;margin-top:4px">Firms report higher staff trust after six months.</div>
  </div>
  <div class="abs" style="left:202px;top:103px;width:70px;height:89px;background:rgba(181,136,58,.9);color:#fff;padding:10px 11px">
    <div style="font-family:'PT Serif',serif;font-size:13px">50%</div>
    <div style="font-size:4.2px;margin-top:4px">Businesses</div>
    <div style="font-size:3.6px;line-height:1.4;margin-top:4px">Teams grow sales in new regions.</div>
    <div style="font-size:3.6px;margin-top:10px">Target Market</div>
  </div>
  <div class="abs" style="left:273px;top:59px;width:69px;height:133px;background:rgba(225,220,220,.78);color:var(--navy);padding:10px 11px">
    <div style="font-family:'PT Serif',serif;font-size:13px">99%</div>
    <div style="font-size:4.2px;margin-top:4px">Branding</div>
    <div style="font-size:3.6px;line-height:1.4;margin-top:4px">Leaders say a clear purpose makes the brand stronger, more trusted and more human in every market.</div>
  </div>
  <div class="foot">The Anatomy of Belonging<span>Page 21</span></div>
</article>

<article class="slide" style="left:413px;top:1967px">
  <div class="brand tl">The Anatomy of Belonging</div>
  <div class="title" style="left:61px;top:37px">Portfolio<br>Three<br>Layout</div>
  <div class="head" style="left:61px;top:87px;font-size:5px;color:var(--ink)">Subtitle</div>
  <div class="txt" style="left:61px;top:95px;width:100px"><b>Real stories show the way.</b> Here we share how teams of many cultures found new trust and lifted results together.<br><br>Each case follows one leader who chose to ask, to listen and to act with care, and the change that followed.</div>
  <div class="photo" style="left:185px;top:0;width:115px;height:208px;background:linear-gradient(170deg,#8f8a80,#6b6a5f 50%,#3d3b36)" role="img" aria-label="Man running on a treadmill"></div>
  <div class="photo" style="left:301px;top:0;width:69px;height:104px;background:linear-gradient(170deg,#6f8b6a,#4c6b55)" role="img" aria-label="Tennis player on a court"></div>
  <div class="photo" style="left:301px;top:106px;width:69px;height:102px;background:linear-gradient(170deg,#c9ccd2,#2c3d8a 60%,#3a3a3a)" role="img" aria-label="Runner in a city race"></div>
  <div class="foot">The Anatomy of Belonging<span>Page 22</span></div>
</article>

<article class="slide" style="left:816px;top:1967px">
  <div class="brand tr">The Anatomy of Belonging</div>
  <div class="photo" style="left:63px;top:34px;width:72px;height:70px;background:linear-gradient(170deg,#d7dbe0,#a7adb5 55%,#8a6e62)" role="img" aria-label="Woman doing yoga on a city rooftop"></div>
  <div class="abs navy" style="left:137px;top:34px;width:70px;height:70px;color:#fff;padding:0 10px">
    <div style="margin-top:40px;font-family:'PT Serif',serif;font-size:4.4px">Conference</div>
    <div style="font-family:'PT Serif',serif;font-size:12px">2019.</div>
  </div>
  <div class="photo" style="left:210px;top:34px;width:126px;height:70px;background:linear-gradient(160deg,#9aa0a5,#5d6267 55%,#3a3d40)" role="img" aria-label="Man holding a side plank on a rooftop"></div>
  <div class="photo" style="left:63px;top:109px;width:85px;height:69px;background:linear-gradient(160deg,#c4a98c,#8d6f57 60%,#5b4a46)" role="img" aria-label="Two people meditating in a studio"></div>
  <div class="photo" style="left:154px;top:109px;width:87px;height:69px;background:linear-gradient(160deg,#4e6a4a,#2f4a35 60%,#1d2d22)" role="img" aria-label="Woman enjoying fresh air among green leaves"></div>
  <div class="photo" style="left:246px;top:109px;width:90px;height:69px;background:linear-gradient(160deg,#f2f2f2,#d9d9d9 60%,#b5b5b5)" role="img" aria-label="Woman meditating in a white room"></div>
  <div class="foot">The Anatomy of Belonging<span>Page 24</span></div>
</article>

</body>
</html>
```